Design business cards for Ironvale Barbers (Opening March so won't need finalised till January2018

Ironvale Barbers is the new age barbers and skincare for all men. Creating tailor made haircuts & customised skincare solutions for the perfect healthy manly look. The Barbers will have a industrial, rustic, worldly feel about it. Rustic red brick wall with old wine barrels as the work stations with the old fashion barber chairs. Concrete floor and a bit corrugated iron around.
Target Market(s)
Professional males who like a great haircut, wet shave and may consider a facial if in the right environment. Total pampering experience in a boys environment.
Industry/Entity Type
Barber
Contact Information for Business Card
Front- Logo - address is 42 Kowhai Rd Taupo
Ph - (07) 548 9163
www.ironvalebarbers.com
email - hello@ironvale.co.nz
Back of card
Mens Haircare - Wet Shaving - Facials - Skin Prescriptions
We are doing a loyalty program - 6 squares numbered then 7th free
Colors
Designer to choose colors to be used in the design.
Requirements
Must have
- Clean simple easy to read.
Nice to have
- Our current colours are white font on black background but thinking we need to introduce another colour. Maybe white logo on a copper, bronze or rusty background. Or even a rustic red brick wall with white writing. Want it clean simple to read. Maybe a burgundy?
Should not have
- no images like heads, scissors, razors please

```html
<!DOCTYPE html>
<html lang="en">
<head>
<meta charset="utf-8">
<title>Ironvale Barbers – Business Cards</title>
<link href="https://fonts.googleapis.com/css2?family=Bebas+Neue&family=Cinzel:wght@600&display=swap" rel="stylesheet">
<style>
  :root {
    --backdrop: #5a4a3c;
    --card-dark: #2a241f;
    --card-mid: #3a322b;
    --ink: #ffffff;
  }
  * { margin: 0; padding: 0; box-sizing: border-box; }
  html, body { width: 1200px; height: 960px; overflow: hidden; }
  body { background: var(--backdrop); position: relative; color: var(--ink); }

  .card {
    position: absolute;
    width: 600px;
    height: 343px;
    box-shadow: 0 2px 4px rgba(0,0,0,.35);
    overflow: hidden;
  }
  .card-surface {
    position: absolute; inset: 0;
    background: linear-gradient(90deg, var(--card-dark), var(--card-mid) 35%, var(--card-dark) 60%, var(--card-mid) 85%, var(--card-dark));
  }
  .card--front { left: 315px; top: 113px; }
  .card--back  { left: 312px; top: 473px; }

  .front-header {
    position: absolute; left: 38px; top: 22px; width: 514px;
    display: flex; align-items: flex-end;
  }
  .holder-name {
    font-family: "Bebas Neue", sans-serif;
    font-size: 70px; line-height: 1; letter-spacing: 0.5px;
    padding-right: 16px; margin-top: 8px;
  }
  .holder-phone {
    font-family: "Bebas Neue", sans-serif;
    border-left: 2px solid var(--ink);
    padding-left: 20px; line-height: .95; margin-bottom: 8px;
  }
  .holder-phone .area { display: block; font-size: 28px; }
  .holder-phone .num  { display: block; font-size: 46px; }

  .rule { position: absolute; left: 38px; width: 514px; height: 2px; background: var(--ink); }
  .rule--1 { top: 94px; }
  .rule--2 { top: 146px; }
  .rule--3 { top: 229px; }

  .address {
    position: absolute; left: 38px; width: 514px; top: 107px;
    text-align: center;
    font-family: "Cinzel", serif; font-size: 19px; letter-spacing: 1px;
  }
  .web {
    position: absolute; left: 38px; width: 520px; top: 155px;
    font-family: "Cinzel", serif; font-size: 29px; line-height: 33px; letter-spacing: 1.5px;
  }
  .services {
    position: absolute; left: 38px; top: 250px;
    font-family: "Bebas Neue", sans-serif; font-size: 25px; letter-spacing: .3px;
  }
  .appointment {
    position: absolute; left: 38px; top: 290px; width: 518px;
    display: flex; align-items: flex-end;
    font-family: "Bebas Neue", sans-serif; font-size: 27px; line-height: 1;
  }
  .appointment .blank { flex: 1; border-bottom: 2px solid var(--ink); height: 22px; }

  .brand {
    position: absolute; inset: 0;
    display: flex; flex-direction: column; align-items: center; justify-content: center;
    font-family: "Bebas Neue", sans-serif; color: var(--ink); line-height: .9;
  }
  .brand-name { font-size: 140px; letter-spacing: 2px; }
  .brand-sub  { font-size: 44px; letter-spacing: 12px; margin-top: 4px; }
</style>
</head>
<body>
  <section class="card card--front">
    <div class="card-surface" role="img" aria-label="Dark weathered wood grain texture"></div>
    <header class="front-header">
      <h1 class="holder-name">DANIEL HARTLEY</h1>
      <p class="holder-phone"><span class="area">027 318</span><span class="num">5962</span></p>
    </header>
    <div class="rule rule--1"></div>
    <p class="address">42 Kowhai Rd Taupo</p>
    <div class="rule rule--2"></div>
    <p class="web">HELLO@IRONVALE.CO.NZ<br>IRONVALEBARBERS.CO.NZ</p>
    <div class="rule rule--3"></div>
    <p class="services">MENS HAIRCARE - WET SHAVING - FACIALS - SKIN PRESCRIPTIONS</p>
    <div class="appointment">
      <span>DATE</span><span class="blank"></span><span>TIME</span><span class="blank"></span>
    </div>
  </section>

  <section class="card card--back">
    <div class="card-surface" role="img" aria-label="Dark weathered wood grain texture"></div>
    <div class="brand">
      <span class="brand-name">IRONVALE</span>
      <span class="brand-sub">BARBERS</span>
    </div>
  </section>
</body>
</html>
```